Flyer-Design für Hundeschule
Zielgruppe
Ich habe eine Hundeschule, seit 11 Jahren, die sich gerade neu aufstellt. Meine Zielgruppe sind junge bis mittel alte Hundemenschen die ihren Hund erziehen möchten und gerne auch ihr Freizeit mit ihm verbringen.
Aufgabenstellung
Ich möchte gerne ein Design was Neukunden anspricht.
Gerne auch, was man sich an den Kühlschrank hängt, weil es so schön ist ;-)
Ich habe sehr viele Fotos vom Profi und kann immer nachliefern, falls deiner Meinung nach etwas nicht ganz passt.
Das Logo habe ich in allen möglichen Dateiformen. Kann ich auch gerne nachliefern.
Vielleicht ist es auch zu viel Text?
Ich bin für alles offen :-)
Die Flyer möchte ich dann bei papier-flott-shop.de bestellen.
Ich freue mich auf deinen Vorschlag!

```html
<!DOCTYPE html>
<html lang="de">
<head>
<meta charset="utf-8">
<title>PfotenPfad – Flyer</title>
<link href="https://fonts.googleapis.com/css2?family=Source+Sans+3:ital,wght@0,400;0,600;0,700;1,400&family=Caveat:wght@600&display=swap" rel="stylesheet">
<style>
:root{
  --stage:#8a8a8a;
  --paper:#ffffff;
  --teal:#6fbcb9;
  --teal-light:#c4e2e0;
  --teal-line:#b5dcda;
  --red:#c9432c;
  --brown:#5b4037;
  --ink:#3a3a3a;
  --frame:#cfe5e4;
}
*{margin:0;padding:0;box-sizing:border-box}
html,body{width:1200px;height:881px;overflow:hidden;background:var(--stage)}
body{position:relative;font-family:"Source Sans 3",sans-serif;color:var(--ink)}
.panel{position:absolute;left:14px;width:1166px;height:411px;background:var(--paper);overflow:hidden}
.panel--front{top:11px}
.panel--back{top:459px}
.abs{position:absolute}
.decor{position:absolute;left:0;top:0}
.photo{position:absolute;border-radius:50%;border:3px solid #fff;box-shadow:0 1px 4px rgba(0,0,0,.35)}
.photo--portrait{left:85px;top:31px;width:170px;height:170px;background:radial-gradient(circle at 40% 40%,#b9a68f,#6a5746)}
.photo--shepherd-mix{left:610px;top:196px;width:188px;height:188px;background:linear-gradient(160deg,#d6a25c 0%,#a6b65a 55%,#6f8f3a 100%)}
.photo--shepherd{left:828px;top:233px;width:164px;height:164px;background:linear-gradient(170deg,#8a5f8a 0%,#7b6a45 45%,#a07a4a 100%)}
.photo--hound{left:1020px;top:200px;width:130px;height:130px;background:linear-gradient(150deg,#e0cf84 0%,#b08a4a 50%,#7a4e2e 100%)}
.photo--bulldogs{left:9px;top:132px;width:170px;height:170px;background:linear-gradient(180deg,#b8c0b0 0%,#e8e6e0 45%,#7aa05a 100%)}
.intro{position:absolute;left:291px;top:36px;width:256px;color:#fff;font-size:11.4px;line-height:15.7px;text-align:center}
.intro p{margin-bottom:5px}
.intro strong{font-weight:700}
.signature{position:absolute;left:291px;top:193px;width:256px;text-align:center;color:#fff;font-family:"Caveat",cursive;font-size:28px;line-height:30px}
.brand-name{position:absolute;left:818px;top:66px;width:330px;font-size:62px;line-height:70px;font-weight:600;color:var(--red);letter-spacing:1px}
.brand-tagline{position:absolute;left:818px;top:164px;width:330px;text-align:center;font-size:20px;line-height:24px;font-weight:600;color:var(--brown);letter-spacing:.6px}
.web-url{position:absolute;left:20px;top:338px;width:545px;text-align:center;font-size:27.5px;line-height:32px;font-weight:700;color:var(--red)}
.contact{position:absolute;left:20px;top:383px;width:545px;text-align:center;font-size:9px;line-height:12px;color:#555}
.box{position:absolute;top:23px;width:554px;height:366px;border:1px solid var(--frame)}
.box--left{left:14px}
.box--right{left:600px}
.line{position:absolute;white-space:nowrap;font-size:10px;line-height:12px}
.h{color:var(--red);font-weight:700}
.line em,.course-info{font-style:italic}
b{font-weight:700}
.col{position:absolute;font-size:10px;line-height:12.9px}
.col .h{display:block}
.col ul{list-style:none}
.col li{position:relative;padding-left:16px}
.col li::before{content:"•";position:absolute;left:1px}
.col .note{font-style:italic}
.cta{position:absolute;width:250px;height:34px;background:var(--teal-light);border-radius:4px;text-align:center;font-size:10px;line-height:13px;font-weight:700;color:var(--ink);padding-top:4px}
.cta span{color:var(--red)}
.credit{position:absolute;left:882px;top:354px;width:250px;text-align:center;font-size:9.5px;font-style:italic;color:#888}
</style>
</head>
<body>

<section class="panel panel--front">
  <svg class="decor" width="1166" height="411" viewBox="0 0 1166 411">
    <polygon points="0,0 709,0 611,318 0,218" fill="var(--teal)"/>
    <polygon points="0,231 475,308 475,312 0,236" fill="var(--teal-line)"/>
    <polygon points="0,251 257,291 257,295 0,256" fill="var(--teal-line)" opacity=".8"/>
    <polygon points="0,274 116,291 116,295 0,279" fill="var(--teal-line)" opacity=".7"/>
    <polygon points="763,411 1166,346 1166,351 790,411" fill="var(--teal-line)"/>
    <polygon points="880,411 1166,372 1166,376 905,411" fill="var(--teal-line)" opacity=".6"/>
  </svg>

  <div class="photo photo--portrait" role="img" aria-label="Sepia-Porträt der Trainerin mit ihrem Hund"></div>

  <div class="intro">
    <p>Mein Name ist Katrin Albers, geb. 1986 in Halle. Meine Leben teile ich mit meinem Mann, unserer Tochter, unseren vier Hunden und vier Katzen im schönen Birkenhain in Lindental.</p>
    <p>Seit 2009 bin ich Hundetrainerin aus Leidenschaft. <strong>Ich setze alles daran, dass Mensch und Hund durch meine Hilfe (wieder) ein Team werden.</strong></p>
    <p>Ich freue mich auf dich und deine Fellnase(n)!<br>Liebe Grüße und hab eine gute Zeit,</p>
  </div>
  <div class="signature">Katrin Albers</div>

  <div class="brand-name">PfotenPfad</div>
  <div class="brand-tagline">Hundetraining für jede Schnauze</div>

  <div class="photo photo--shepherd-mix" role="img" aria-label="Hund im gelben Geschirr schaut zur Trainerin auf"></div>
  <div class="photo photo--shepherd" role="img" aria-label="Schäferhund liegt neben einem Pylon"></div>
  <div class="photo photo--hound" role="img" aria-label="Brauner Jagdhund sitzt im Herbstlaub"></div>

  <div class="web-url">www.hundetraining-PfotenPfad.de</div>
  <div class="contact">| Hundetraining PfotenPfad (ehemals Hundeschule Berger) | Katrin Albers | Am Lindenhof 7 | 06100 Lindental |<br>Mail: info@hundetraining-pfotenpfad.de | Telefon/WhatsApp: 0170-482 196 35</div>
</section>

<section class="panel panel--back">
  <div class="box box--left"></div>
  <div class="box box--right"></div>

  <div class="line h" style="left:41px;top:41px">Exklusives Einzeltraining oder doch gemeinsam in einer Hundegruppe lernen?</div>
  <div class="line" style="left:41px;top:56px">Ich biete dir eine individuelle Lösung.</div>
  <div class="line h" style="left:41px;top:75px">Training in der Gruppe:</div>
  <div class="line" style="left:41px;top:88px">Gemeinsam lernen macht Spaß und fördert das sozialverhalten deines Hundes.</div>
  <div class="line" style="left:41px;top:100px">Alle Kurse finden in 06100 Lindental OT Birkenhain statt.</div>
  <div class="line" style="left:132px;top:116px">• <b>Welpenkurs</b>: Wir legen gemeinsam den optimalen Grundstein für einen sozialen und</div>
  <div class="line" style="left:153px;top:129px">ruhigen Hund.</div>
  <div class="line" style="left:167px;top:142px"><em>– Anmeldung bis zur 14. Lebenswoche, Einstieg jederzeit möglich, Dauer 8 Wochen,</em></div>
  <div class="line" style="left:176px;top:155px"><em>Kursgebühr 120 € –</em></div>
  <div class="line" style="left:182px;top:168px">• <b>Junghundkurs</b>: Zusammenwachsen und aus dem jungen Wilden einen tollen</div>
  <div class="line" style="left:188px;top:181px">Begleiter machen.</div>
  <div class="line" style="left:190px;top:194px"><em>– Anmeldung ab dem 4.- 10. Monat, Dauer: 12 Wochen, Einstieg alle 6 Wochen</em></div>
  <div class="line" style="left:190px;top:207px"><em>möglich, Kursgebühr 180 € –</em></div>
  <div class="line" style="left:191px;top:220px">• <b>Benimm dich! - Kurs</b> – die vier Säulen des guten Benehmens in Perfektion.</div>
  <div class="line" style="left:192px;top:233px">• Modul 1: Sicherer Rückruf</div>
  <div class="line" style="left:189px;top:246px">• Modul 2: Entspanntes gehen an der Leine</div>
  <div class="line" style="left:182px;top:259px">• Modul 3: Führen und Folgen</div>
  <div class="line" style="left:173px;top:272px">• Modul 4: Sitz-Platz-Bleib in Perfektion</div>
  <div class="line" style="left:164px;top:285px"><em>– Anmeldung ab dem 10. Lebensmonat, Dauer 4 Wochen je Modul, Einstieg</em></div>
  <div class="line" style="left:149px;top:298px"><em>alle 4 Wochen möglich, Je Modul 60€, alle Module zusammen 220€ –</em></div>
  <div class="line" style="left:41px;top:317px"><b>Workshops</b>: Manchmal hat man nur dieses eine, ganz spezielle Thema mit seinem Hund. Und man möchte</div>
  <div class="line" style="left:41px;top:330px">genau hieran trainieren. Dann sind meine Workshops genau das Richtige. Immer wieder gibt es neue Themen,</div>
  <div class="line" style="left:41px;top:343px">wie zum Beispiel <em>„Die andere Art der Leinenführung“</em> oder <em>„Der perfekte Rückruf“.</em></div>
  <div class="line" style="left:41px;top:358px">Wir trainieren hier in kleinen Gruppen, um dein Ziel zu erreichen.</div>

  <div class="photo photo--bulldogs" role="img" aria-label="Zwei weiße Hunde spielen mit einem Seil auf der Wiese"></div>

  <div class="col" style="left:625px;top:42px;width:246px">
    <span class="h">Lust auf Abenteuer und Spaß? Verbringe Zeit mit deinem Hund in meinen Beschäftigungskursen:</span>
    <ul>
      <li><b>Crossdogging</b>: Du und dein Hund stellen sich wöchentlich neuen spannenden Aufgaben. Hier lernst du auch in Stresssituationen ruhig zu bleiben.</li>
      <li><b>Rally Obedience</b>: Geschicklichkeit und Gehorsam gepaart mit jeder Menge Spaß.</li>
      <li><b>Longieren</b>: Distanz schafft Nähe! Du arbeitest mit deinem Hund über die Distanz am Longierkreis. Ein toller Sport für den Aufbau einer harmonischen Bindung und Beziehung.</li>
    </ul>
  </div>
  <div class="cta" style="left:615px;top:192px">Sichere dir jetzt deinen Platz im Kurs oder Workshop<br>unter: <span>www.hundetraining-PfotenPfad.de</span></div>
  <div class="col" style="left:625px;top:238px;width:246px">
    <span class="h">Exklusives Einzeltraining</span>
    Im Einzeltraining liegt mein ganze Aufmerksamkeit nur bei dir und deinem Hund. Die Trainings finden je nach Art bei dir Zuhause oder in Lindental/ OT Birkenhain statt.
    <ul>
      <li><b>Problemhundtherapie:</b> Dein Hund kann nicht alleine bleiben, zeigt Aggressionen in jeglicher Ausprägung oder ist ein ängstlicher Hund? Dann bist du bei mir genau richtig. Zusammen suchen wir nach der Ursache des Verhaltens, denn diese</li>
    </ul>
  </div>

  <div class="col" style="left:889px;top:42px;width:232px">
    <ul>
      <li style="padding-left:16px" class="cont">ist Auslöser des gezeigten Problems. Zusammen arbeiten wir uns Schritt für Schritt aus dem Problemverhalten heraus, hin zu einer harmonischen Mensch-Hund-Beziehung.<br><span class="note">(Training vorrangig bei dir Zuhause)</span></li>
      <li><b>Grunderziehung für Hunde ab 6 Monaten:</b> Ich zeige dir, wie du deinen Hund zu einem perfekten Begleiter machen kannst. Egal ob du ihn gerade aus dem Tierheim adoptiert, von privat übernommen hast oder er schon länger bei dir ist. Die kleinen Probleme des Alltags (Leineziehen, anspringen o.ä) werden wir schnell lösen. Es ist nie zu spät für eine tolle Mensch-Hund-Beziehung.<br><span class="note">(Training vorrangig in Lindental)</span></li>
      <li><b>Welpenerziehung:</b> Ich zeige dir, wie du eine gute Basis schaffst, in der sich dein Welpe sicher fühlen kann. Dabei spielt gute Sozialisation natürlich eine große Rolle. All das wirst du im meinem Training, zusammen mit deinem Hund lernen.<br><span class="note">(Training vorrangig in Lindental)</span></li>
    </ul>
  </div>
  <div class="cta" style="left:882px;top:313px">Buche jetzt dein exklusives Einzeltraining unter:<br><span>www.hundetraining-PfotenPfad.de</span></div>
  <div class="credit">© Fotografien: Pfotenblick (Lena Hoffmann)</div>
</section>

<style>.col li.cont::before{content:""}</style>
</body>
</html>
```